" Atendimento individual, observando as necessidades do aluno com especial atenção às lacunas de conhecimento (conteúdos que não foram aprendidos/absorvidos adequadamente e que dificultam a compreensão de novos tópicos). Para tanto, preparamos aulas exclusivas para cada aluno, que é sempre visto como um indivíduo independente que devem ter suas necessidades respeitadas. Dessa forma, trabalhamos para estimular conhecimento, criatividade e autonomia, para vencer dificuldades, enfrentar desafios e formar organização pessoal através de um horário fixo de estudos. "

```html
<!DOCTYPE html>
<html lang="pt-BR">
<head>
<meta charset="UTF-8">
<title>Clara Moreira – Espaço Educacional · Cartão de visita</title>
<link rel="stylesheet" href="https://fonts.googleapis.com/css2?family=Marcellus&family=Arimo:wght@400;700&display=swap">
<style>
  :root {
    --canvas: #e4e4e4;
    --card-white: #ffffff;
    --brand: #a5644f;
    --brand-dark: #93533f;
    --brand-light: #b5765f;
    --ink-grey: #555555;
    --line-light: rgba(255, 255, 255, 0.55);
  }
  * { box-sizing: border-box; margin: 0; padding: 0; }
  html, body {
    width: 1200px; height: 1200px; overflow: hidden;
    background: var(--canvas);
  }
  .sheet {
    position: relative; width: 1200px; height: 1200px;
    display: flex; flex-direction: column; align-items: center;
    justify-content: center; gap: 52px;
  }
  .card {
    position: relative; width: 900px; height: 514px; overflow: hidden;
    box-shadow: 0 10px 28px rgba(0, 0, 0, 0.18);
  }

  /* Front */
  .card--front { background: var(--card-white); }
  .brand-lockup {
    position: absolute; left: 0; right: 0; top: 170px;
    display: flex; flex-direction: column; align-items: center;
    color: var(--brand); font-family: "Marcellus", serif; font-weight: 400;
  }
  .brand-lockup__row { display: flex; align-items: center; gap: 22px; }
  .brand-lockup__dot {
    width: 44px; height: 44px; border-radius: 50%; background: var(--brand);
  }
  .brand-lockup__name { font-size: 68px; letter-spacing: 1px; line-height: 1; }
  .brand-lockup__tagline {
    margin: 10px 0 0 66px; font-size: 22px; letter-spacing: 9px; text-transform: uppercase;
  }
  .front-web {
    position: absolute; left: 470px; bottom: 36px;
    font-family: "Arimo", sans-serif; font-weight: 700; font-size: 17px;
    color: var(--ink-grey); letter-spacing: 1px;
  }
  .front-bar {
    position: absolute; left: 300px; bottom: 0; width: 330px; height: 22px;
    background: var(--brand);
  }

  /* Back */
  .card--back { background: var(--card-white); }
  .back-field {
    position: absolute; left: 0; top: 0; width: 100%; height: 330px;
    background: linear-gradient(180deg, var(--brand-light), var(--brand) 55%, var(--brand-dark));
  }
  .back-watermark {
    position: absolute; left: 0; right: 0; top: 22px; text-align: center;
    font-family: "Marcellus", serif; font-size: 52px; color: rgba(255, 255, 255, 0.12);
  }
  .back-rule {
    position: absolute; left: 0; width: 100%; height: 2px; background: var(--line-light);
  }
  .back-rule--top { top: 100px; }
  .back-rule--mid { top: 178px; }
  .back-name {
    position: absolute; left: 0; right: 0; top: 124px; line-height: 30px; text-align: center;
    font-family: "Arimo", sans-serif; font-size: 24px; letter-spacing: 2px;
    color: var(--card-white); text-transform: uppercase;
  }
  .contact-stem {
    position: absolute; top: 180px; width: 2px; height: 52px; background: var(--line-light);
  }
  .contact-icon { position: absolute; top: 230px; width: 44px; height: 44px; }
  .contact-pointer { position: absolute; top: 306px; width: 48px; height: 25px; }
  .contact-text {
    position: absolute; top: 356px; white-space: nowrap;
    font-family: "Arimo", sans-serif; font-size: 20px; line-height: 1.5;
    color: var(--ink-grey);
  }
  .contact-text--phone { left: 60px; }
  .contact-text--email { left: 330px; }
  .contact-text--address { left: 556px; }
</style>
</head>
<body>
<main class="sheet">

  <section class="card card--front" aria-label="Frente do cartão">
    <div class="brand-lockup">
      <div class="brand-lockup__row">
        <span class="brand-lockup__dot"></span>
        <span class="brand-lockup__name">Clara Moreira</span>
      </div>
      <span class="brand-lockup__tagline">Espaço Educacional</span>
    </div>
    <p class="front-web">www.site.com.br</p>
    <div class="front-bar"></div>
  </section>

  <section class="card card--back" aria-label="Verso do cartão">
    <div class="back-field"></div>
    <p class="back-watermark">Clara Moreira</p>
    <div class="back-rule back-rule--top"></div>
    <div class="back-rule back-rule--mid"></div>
    <p class="back-name">Clara Moreira</p>

    <div class="contact-stem" style="left:199px"></div>
    <div class="contact-stem" style="left:441px"></div>
    <div class="contact-stem" style="left:719px"></div>

    <svg class="contact-icon" style="left:178px" viewBox="0 0 44 44" aria-label="Telefone">
      <circle cx="22" cy="22" r="20" fill="none" stroke="#fff" stroke-width="2"/>
      <path d="M16 13c1.5-1 3 0 3.5 1.5l1 3c.3 1-.3 1.8-1 2.3-.6.5-.5 1.3 0 2l1.7 2.2c.6.7 1.4.9 2 .4.8-.6 1.8-.8 2.6-.2l2.5 2c1.2 1 1 2.6-.2 3.6-3 2.5-8.5-.5-11.5-5.2-2.6-4-3-9.2-.6-11.4z" fill="#fff"/>
    </svg>
    <svg class="contact-icon" style="left:420px" viewBox="0 0 44 44" aria-label="E-mail">
      <circle cx="22" cy="22" r="20" fill="none" stroke="#fff" stroke-width="2"/>
      <text x="22" y="29" text-anchor="middle" font-family="Arimo, sans-serif" font-size="20" fill="#fff">@</text>
    </svg>
    <svg class="contact-icon" style="left:698px" viewBox="0 0 44 44" aria-label="Endereço">
      <circle cx="22" cy="22" r="20" fill="none" stroke="#fff" stroke-width="2"/>
      <path d="M22 11a7 7 0 0 0-7 7c0 5.5 7 14 7 14s7-8.5 7-14a7 7 0 0 0-7-7zm0 10a3 3 0 1 1 0-6 3 3 0 0 1 0 6z" fill="#fff"/>
    </svg>

    <svg class="contact-pointer" style="left:176px" viewBox="0 0 48 25"><path d="M0 25 L24 0 L48 25 Z" fill="#fff"/></svg>
    <svg class="contact-pointer" style="left:418px" viewBox="0 0 48 25"><path d="M0 25 L24 0 L48 25 Z" fill="#fff"/></svg>
    <svg class="contact-pointer" style="left:696px" viewBox="0 0 48 25"><path d="M0 25 L24 0 L48 25 Z" fill="#fff"/></svg>

    <p class="contact-text contact-text--phone">+ 00-00 0000-0000<br>+ 00-00 0000-0000</p>
    <p class="contact-text contact-text--email">email@exemplo.com</p>
    <p class="contact-text contact-text--address">Endereço Completo | Rua | Nº<br>Bairro | Cidade | CEP | UF | Brasil</p>
  </section>

</main>
</body>
</html>
```